Corrigan's Irish Pub Menu Design

New menu design for Corrigan's Irish Pub prefer someone with menu design experience. Menu items are attached and I'll need working files to make updates. The design should be 8.5"x14" 1 cover page and 3 page menu if possible or 4 page menu if not with a Header on the first page this is for print and web. Please include the new logo and it should be in a traditional Irish Pub style. When complete please send a proof for markup (watermark is fine just want to markup and proof) and I'll send back for revisions.
Colors
Designer to choose colors to be used in the design.
Look and feel
Each slider illustrates characteristics of the customer's brand and the style your logo design should communicate.

```html
<!DOCTYPE html>
<html lang="en">
<head>
<meta charset="utf-8">
<title>Corrigan's Irish Pub – Menu Spread</title>
<link href="https://fonts.googleapis.com/css2?family=Josefin+Sans:wght@300;400;600&family=Ubuntu:wght@500&display=swap" rel="stylesheet">
<style>
  :root {
    --backdrop: #9a9b9f;
    --paper: #efeff1;
    --accent: #ff5a00;
    --ink: #2b2b2e;
    --ink-soft: #4a4a4f;
  }
  * { box-sizing: border-box; margin: 0; padding: 0; }
  html, body { width: 1200px; height: 1200px; overflow: hidden; }
  body {
    background: var(--backdrop);
    font-family: "Josefin Sans", sans-serif;
    color: var(--ink);
    position: relative;
  }
  .spread {
    position: absolute;
    left: 40px; top: 147px;
    width: 1120px; height: 906px;
    display: flex;
  }
  .page {
    width: 560px; height: 100%;
    display: flex;
    background: var(--paper);
  }
  .page-photo { flex: 0 0 166px; height: 100%; }
  .photo-nachos {
    background: linear-gradient(180deg, #b27a3a 0%, #c98f48 12%, #e8d8b8 20%, #d9c070 32%, #6f8a3c 42%, #c8643a 52%, #e6dcc6 62%, #d8b460 74%, #f0ece4 82%, #2d2a28 88%, #c58a45 94%, #b27a3a 100%);
  }
  .photo-burger {
    background: linear-gradient(180deg, #4a3a30 0%, #8a6a55 20%, #b08a70 40%, #d56a20 47%, #e07a2a 55%, #f0e4d8 62%, #4a3a32 66%, #3a2c26 70%, #d24a30 73%, #6aa83a 78%, #e8c48a 84%, #8ab0b8 92%, #7aa0aa 100%);
  }
  .accent-rule { flex: 0 0 5px; background: var(--accent); }
  .panel {
    flex: 1;
    padding: 38px 36px 0 32px;
    display: flex; flex-direction: column;
  }
  .section-title {
    font-family: "Ubuntu", sans-serif;
    font-weight: 500;
    color: var(--accent);
    font-size: 22px;
    letter-spacing: 0.5px;
    text-align: center;
  }
  .section-note {
    font-family: "Josefin Sans", sans-serif;
    font-weight: 600;
    font-size: 11px;
    line-height: 15px;
    text-align: center;
    margin-top: 8px;
  }
  .menu-list { list-style: none; }
  .menu-item { margin-bottom: 13px; }
  .item-line {
    display: flex; align-items: baseline;
    font-weight: 300;
    font-size: 16px;
    letter-spacing: 1px;
    text-transform: uppercase;
  }
  .item-name { white-space: nowrap; }
  .item-lead {
    flex: 1;
    border-bottom: 1.5px dotted var(--ink-soft);
    margin: 0 3px;
    transform: translateY(-3px);
  }
  .item-price { white-space: nowrap; font-size: 15px; }
  .item-line.multi { align-items: flex-end; }
  .item-line.multi .item-name { white-space: normal; line-height: 19px; }
  .item-desc {
    font-size: 10px;
    line-height: 13px;
    letter-spacing: 0.5px;
    color: var(--ink-soft);
    margin-top: 2px;
  }
  .appetizers .section-title { margin-top: 6px; margin-bottom: 28px; }
  .soups { margin-top: 28px; }
  .soups .menu-list { margin-top: 22px; }
  .dressings-title { margin-top: 18px; font-size: 20px; letter-spacing: 1.5px; }
  .dressings-list { margin-top: 14px; font-weight: 600; font-size: 12px; line-height: 15px; text-align: center; }
  .right .panel { padding-top: 36px; }
  .right .menu-list { margin-top: 30px; }
  .sandwiches { margin-top: 18px; }
</style>
</head>
<body>
<main class="spread">
  <section class="page left">
    <div class="page-photo photo-nachos" role="img" aria-label="Photo of loaded nachos with guacamole, pico de gallo and sour cream in a basket"></div>
    <div class="accent-rule"></div>
    <div class="panel">
      <div class="appetizers">
        <h2 class="section-title">APPETIZERS</h2>
        <ul class="menu-list">
          <li class="menu-item"><div class="item-line"><span class="item-name">Irish Tacos</span><span class="item-lead"></span><span class="item-price">2/9 - 3/11</span></div></li>
          <li class="menu-item"><div class="item-line"><span class="item-name">Steak Bites</span><span class="item-lead"></span><span class="item-price">2</span></div></li>
          <li class="menu-item"><div class="item-line"><span class="item-name">Poutine</span><span class="item-lead"></span><span class="item-price">13</span></div></li>
          <li class="menu-item"><div class="item-line"><span class="item-name">Irish Potato Skins</span><span class="item-lead"></span><span class="item-price">13</span></div></li>
          <li class="menu-item"><div class="item-line"><span class="item-name">Fish Spread</span><span class="item-lead"></span><span class="item-price">10</span></div></li>
          <li class="menu-item"><div class="item-line multi"><span class="item-name">Jalapeno Pimiento<br>Cheese Spread</span><span class="item-lead"></span><span class="item-price">10</span></div></li>
          <li class="menu-item"><div class="item-line"><span class="item-name">Pretzel Dippers</span><span class="item-lead"></span><span class="item-price">12</span></div></li>
          <li class="menu-item"><div class="item-line"><span class="item-name">Irish Nachos</span><span class="item-lead"></span><span class="item-price">12</span></div></li>
          <li class="menu-item"><div class="item-line"><span class="item-name">Pickle Fries</span><span class="item-lead"></span><span class="item-price">9</span></div></li>
          <li class="menu-item"><div class="item-line"><span class="item-name">Dunmore Gravy Fries</span><span class="item-lead"></span><span class="item-price">9</span></div></li>
          <li class="menu-item"><div class="item-line"><span class="item-name">Corrigan's Chicken Wings</span><span class="item-lead"></span><span class="item-price">11</span></div>
            <p class="item-desc">Beer Brined, Dry-Rubbed and Deep Fry with your choice of: Dunmore Buffalo Sauce, Whiskey Teriyaki - Corrigan BBQ, Garlic Butter Parmesan, Grapefruit Habanero<br>Served with Celery and choice of Ranch or Blue Cheese<br>(One Sauce per Order)</p></li>
        </ul>
      </div>
      <div class="soups">
        <h2 class="section-title">SOUPS AND SALADS</h2>
        <p class="section-note">ASK ABOUT THE CHEF'S SOUPS<br>CUP 4, BOWL 6<br>Served with Roll</p>
        <ul class="menu-list">
          <li class="menu-item"><div class="item-line"><span class="item-name">Irish Potato Salad</span><span class="item-lead"></span><span class="item-price">Half/9, Full 12</span></div></li>
          <li class="menu-item"><div class="item-line"><span class="item-name">Garden Salad</span><span class="item-lead"></span><span class="item-price">Half/6, Full 10</span></div></li>
        </ul>
        <h3 class="section-title dressings-title">Dressings:</h3>
        <p class="dressings-list">Add Grilled or Blackend Chicken/5<br>Add Grilled or Blackend Salmon<br>Add Beef Tips / 9<br>Add Corned Beef / 5</p>
      </div>
    </div>
  </section>

  <section class="page right">
    <div class="page-photo photo-burger" role="img" aria-label="Photo of a sesame-bun burger with beef patty, tomato and lettuce"></div>
    <div class="accent-rule"></div>
    <div class="panel">
      <div class="burgers">
        <h2 class="section-title">PUB BURGERS</h2>
        <p class="section-note">Served With Your Choice of<br>Add Horseradishslaw, Mashed Potato</p>
        <ul class="menu-list">
          <li class="menu-item"><div class="item-line"><span class="item-name">The Blarney Burger</span><span class="item-lead"></span><span class="item-price">11</span></div></li>
          <li class="menu-item"><div class="item-line"><span class="item-name">The Black and Blue Burger</span><span class="item-lead"></span><span class="item-price">12</span></div></li>
          <li class="menu-item"><div class="item-line"><span class="item-name">The Southern Burger</span><span class="item-lead"></span><span class="item-price">12</span></div></li>
          <li class="menu-item"><div class="item-line"><span class="item-name">The Melt</span><span class="item-lead"></span><span class="item-price">12</span></div></li>
          <li class="menu-item"><div class="item-line"><span class="item-name">The Shine</span><span class="item-lead"></span><span class="item-price">13</span></div></li>
        </ul>
      </div>
      <div class="sandwiches">
        <h2 class="section-title">PUB SANDWICHES</h2>
        <p class="section-note">Served With Your Choice of<br>Add Horseradishslaw, Mashed Potato</p>
        <ul class="menu-list">
          <li class="menu-item"><div class="item-line"><span class="item-name">Reubew</span><span class="item-lead"></span><span class="item-price">12</span></div></li>
          <li class="menu-item"><div class="item-line"><span class="item-name">Rachel</span><span class="item-lead"></span><span class="item-price">12</span></div></li>
          <li class="menu-item"><div class="item-line"><span class="item-name">Classic Grilled Chicken</span><span class="item-lead"></span><span class="item-price">12</span></div></li>
          <li class="menu-item"><div class="item-line"><span class="item-name">The Celtic Chicken</span><span class="item-lead"></span><span class="item-price">11</span></div></li>
          <li class="menu-item"><div class="item-line"><span class="item-name">The Corrigan</span><span class="item-lead"></span><span class="item-price">13</span></div></li>
          <li class="menu-item"><div class="item-line"><span class="item-name">Grilled Pimento Cheese</span><span class="item-lead"></span><span class="item-price">11</span></div></li>
          <li class="menu-item"><div class="item-line"><span class="item-name">Veggie Burger</span><span class="item-lead"></span><span class="item-price">11</span></div></li>
          <li class="menu-item"><div class="item-line"><span class="item-name">The Big Turkey</span><span class="item-lead"></span><span class="item-price">12</span></div>
            <p class="item-desc">Smoked Turkey Apple Wood, Bacon, Swiss, Lettuce, Tomato, Red Onion and Casun Ranch on Grilled Sourdough</p></li>
          <li class="menu-item"><div class="item-line"><span class="item-name">Salmon BLT</span><span class="item-lead"></span><span class="item-price">13</span></div>
            <p class="item-desc">Grilled Salmon, Applewood, Bacon, Lettuce, Tomato and a Roasted Garlic and Tayme on Grilled Sourdough</p></li>
          <li class="menu-item"><div class="item-line"><span class="item-name">BBQ Pork</span><span class="item-lead"></span><span class="item-price">12</span></div>
            <p class="item-desc">Polled Pork, Colesalaw, Pickles and Corrigan BBQ Sauce on a Potato Roll</p></li>
        </ul>
      </div>
    </div>
  </section>
</main>
</body>
</html>
```